Silverleaf Fiscal Scholars Track

size of ad Full: 7” x 9.6”
1- this is for a ladies program so it should appeal to women.
2-however, I do not want any pictures of people in this ad.
3-all the text should be seen and not covered over by graphics.
4-It should be an ad that will draw people's attention and people should look at it and say it looks nice I want to see that ad.
5-I have put all the instructions in yellow in the file below.
6-please leave 1 inch for the footer .
good luck with this project

Need extra days to review

• no picture or vector of people.

```html
<!DOCTYPE html>
<html lang="en">
<head>
<meta charset="utf-8">
<title>Silverleaf Fiscal Scholars Track</title>
<link rel="stylesheet" href="https://fonts.googleapis.com/css2?family=Bebas+Neue&family=Oswald:wght@500&family=Poppins:wght@400;500;600;700;800&display=swap">
<style>
  :root {
    --backdrop: #c4c4c4;
    --lilac: #b49ccd;
    --magenta: #d0105a;
    --butter: #f6f09a;
    --cream: #fbf9f0;
    --navy: #1f2f5a;
    --band: #243b6b;
    --sky: #1e88e5;
    --gold: #f7c92a;
    --lightblue: #5fb8ff;
    --seal: #d3121c;
    --white: #ffffff;
    --ink: #222222;
  }
  * { margin: 0; padding: 0; box-sizing: border-box; }
  html, body { width: 1200px; height: 613px; overflow: hidden; background: var(--backdrop); }
  .flyer {
    position: absolute; left: 390px; top: 18px; width: 420px; height: 576px;
    overflow: hidden; background: var(--cream);
    box-shadow: 0 4px 14px rgba(0,0,0,.18);
    font-family: "Poppins", sans-serif;
  }
  .flyer-shapes { position: absolute; inset: 0; }
  .abs { position: absolute; }
  .kicker {
    left: 0; right: 0; top: 10px; text-align: center;
    font-family: "Oswald", sans-serif; font-weight: 500; font-size: 28px;
    letter-spacing: 6px; color: var(--white);
  }
  .cap-art { left: 258px; top: 58px; width: 158px; height: 80px; }
  .tilted { transform: rotate(-4deg); transform-origin: left bottom; }
  .career { left: 33px; top: 238px; color: var(--white); font-weight: 700; font-size: 11.5px; line-height: 13px; }
  .career-strong { color: var(--gold); font-weight: 800; font-size: 17px; line-height: 19px; margin-top: 2px; }
  .divider { left: 206px; top: 228px; width: 1.5px; height: 62px; background: rgba(255,255,255,.8); }
  .sectors { left: 234px; top: 222px; color: var(--white); }
  .sectors-lead { font-size: 10px; line-height: 13px; font-weight: 500; }
  .sectors-main { font-family: "Bebas Neue", sans-serif; font-size: 32px; line-height: 27px; }
  .advantage { left: 231px; top: 303px; color: var(--navy); }
  .advantage-title { font-weight: 800; font-size: 21px; line-height: 22px; }
  .advantage-list { list-style: none; margin-top: 8px; font-size: 10px; line-height: 17px; color: var(--ink); }
  .advantage-list li { display: flex; align-items: flex-start; gap: 6px; }
  .advantage-list svg { flex: none; margin-top: 3px; }
  .advantage-list .wrap { line-height: 11px; padding-top: 2px; }
  .open-house { left: 19px; top: 338px; display: flex; align-items: center; gap: 7px; }
  .open-house-mark { width: 32px; height: 32px; background: var(--sky); border-radius: 6px; }
  .open-house-text { color: var(--sky); font-weight: 700; font-size: 17px; line-height: 16px; }
  .open-house-text span { display: block; font-size: 13.5px; }
  .event-date { left: 17px; top: 376px; color: var(--magenta); font-weight: 800; font-size: 37px; letter-spacing: -1px; line-height: 40px; }
  .event-time { left: 18px; top: 416px; font-size: 10.5px; letter-spacing: 5.5px; color: var(--ink); }
  .event-info { left: 18px; top: 431px; font-size: 6.3px; color: var(--ink); }
  .event-contact { left: 18px; top: 440px; font-size: 8.3px; color: var(--ink); }
  .event-contact b { color: var(--sky); font-weight: 600; }
  .rating-badge { left: 17px; top: 460px; width: 41px; height: 47px; background: var(--white); border: 1px solid #ccc; display: flex; align-items: center; justify-content: center; }
  .rating-badge i { width: 22px; height: 22px; border-radius: 50%; background: #f08a1c; display: block; }
  .partner { left: 76px; top: 461px; color: var(--white); }
  .partner-name { color: var(--gold); font-weight: 800; font-size: 13.4px; line-height: 15px; }
  .partner-program { color: var(--lightblue); font-weight: 700; font-size: 7px; line-height: 9px; }
  .partner-note { font-size: 6.8px; line-height: 9px; }
  .partner-link { font-weight: 600; font-size: 7px; margin-top: 6px; letter-spacing: .2px; }
  .seal { left: 324px; top: 437px; width: 72px; height: 72px; }
</style>
</head>
<body>
<main class="flyer" aria-label="Silverleaf Fiscal Scholars Track advertisement">
  <svg class="flyer-shapes" viewBox="0 0 420 576" width="420" height="576" aria-hidden="true">
    <defs>
      <linearGradient id="mistFade" x1="0" y1="0" x2="0" y2="1">
        <stop offset="0" stop-color="#d6eaef"/>
        <stop offset="1" stop-color="#fbf8ee"/>
      </linearGradient>
    </defs>
    <polygon points="0,0 420,0 420,102 0,152" fill="var(--lilac)"/>
    <polygon points="0,152 420,102 420,270 0,323" fill="var(--magenta)"/>
    <polygon points="0,323 189,299 220,457 0,457" fill="url(#mistFade)"/>
    <polygon points="189,299 420,270 420,457 220,457" fill="var(--butter)"/>
    <rect x="0" y="457" width="420" height="52" fill="var(--band)"/>
    <g transform="rotate(-4 34 231)" fill="var(--white)" font-family="'Bebas Neue', sans-serif">
      <text x="30" y="98" font-size="46" textLength="128" lengthAdjust="spacingAndGlyphs">A MASTER’S</text>
      <text x="31" y="142" font-size="58" textLength="150" lengthAdjust="spacingAndGlyphs">DEGREE IN</text>
      <text x="33" y="229" font-size="114" textLength="338" lengthAdjust="spacingAndGlyphs">ACCOUNTING</text>
    </g>
  </svg>

  <div class="abs kicker">ATTENTION WOMEN</div>
  <svg class="abs cap-art" viewBox="0 0 158 80" role="img" aria-label="Graduation cap with red tassel illustration">
    <defs>
      <linearGradient id="capTone" x1="0" y1="0" x2="0" y2="1">
        <stop offset="0" stop-color="#2b2b2b"/>
        <stop offset="1" stop-color="#111"/>
      </linearGradient>
    </defs>
    <rect width="158" height="80" rx="10" fill="url(#capTone)"/>
  </svg>

  <div class="abs career tilted">
    A STABLE, LUCRATIVE<br>CAREER WITH
    <div class="career-strong">HIGH-PAYING<br>FULL /PART TIME</div>
  </div>
  <div class="abs divider tilted"></div>
  <div class="abs sectors tilted">
    <div class="sectors-lead">Opportunities in</div>
    <div class="sectors-main">PRIVATE/PUBLIC<br>COMPANIES</div>
  </div>

  <section class="abs advantage">
    <h2 class="advantage-title">THE NVC JOB<br>PLACEMENT<br>ADVANTAGE</h2>
    <ul class="advantage-list">
      <li><svg width="9" height="9" viewBox="0 0 10 10"><circle cx="5" cy="5" r="4.3" fill="none" stroke="var(--seal)" stroke-width="1.1"/><path d="M3 5.2 4.5 6.6 7.2 3.6" fill="none" stroke="var(--seal)" stroke-width="1.2"/></svg>96% Placement Rate</li>
      <li><svg width="9" height="9" viewBox="0 0 10 10"><circle cx="5" cy="5" r="4.3" fill="none" stroke="var(--seal)" stroke-width="1.1"/><path d="M3 5.2 4.5 6.6 7.2 3.6" fill="none" stroke="var(--seal)" stroke-width="1.2"/></svg>6 placement directors</li>
      <li><svg width="9" height="9" viewBox="0 0 10 10"><circle cx="5" cy="5" r="4.3" fill="none" stroke="var(--seal)" stroke-width="1.1"/><path d="M3 5.2 4.5 6.6 7.2 3.6" fill="none" stroke="var(--seal)" stroke-width="1.2"/></svg><span class="wrap">Decades of relationships<br>with 100’s of firms</span></li>
    </ul>
  </section>

  <div class="abs open-house">
    <div class="open-house-mark"></div>
    <div class="open-house-text">MEETLINE<span>OPEN HOUSE</span></div>
  </div>
  <div class="abs event-date">JUNE 14</div>
  <div class="abs event-time">SUNDAY @2PM</div>
  <div class="abs event-info">for a meetline link / conference number /information</div>
  <div class="abs event-contact"><b>info@nvccareers.org</b> or <b>555 014 2200 x 108</b></div>

  <div class="abs rating-badge"><i></i></div>
  <div class="abs partner">
    <div class="partner-name">HARROWGATE CREST UNIVERSITY</div>
    <div class="partner-program">Masters in Accounting program</div>
    <div class="partner-note">Received the highest possible rating in USA</div>
    <div class="partner-link">HTTPS://HARROWGATECREST.EDU/MSA-RATING</div>
  </div>

  <svg class="abs seal" viewBox="0 0 78 78" aria-label="Masters in 12 months">
    <polygon fill="var(--seal)" points="39,1 44,7 51,3 54,10 62,9 62,16 70,18 67,25 74,30 69,35 76,39 69,43 74,48 67,53 70,60 62,62 62,69 54,68 51,75 44,71 39,77 34,71 27,75 24,68 16,69 16,62 8,60 11,53 4,48 9,43 2,39 9,35 4,30 11,25 8,18 16,16 16,9 24,10 27,3 34,7"/>
    <circle cx="39" cy="39" r="28" fill="none" stroke="var(--white)" stroke-width="1.2"/>
    <text x="39" y="25" text-anchor="middle" font-family="Poppins, sans-serif" font-size="7" font-weight="600" fill="var(--white)">Masters in</text>
    <text x="39" y="48" text-anchor="middle" font-family="Poppins, sans-serif" font-size="25" font-weight="800" fill="var(--white)">12</text>
    <text x="39" y="58" text-anchor="middle" font-family="Poppins, sans-serif" font-size="8" font-weight="700" fill="var(--white)">MONTHS</text>
  </svg>
</main>
</body>
</html>
```